PDN Letterhead

We need a letterhead design that will be able to be used on all marketing products (letterhead, mail chimp, envelops, business cards, etc.) We are a law firm specializing primarily in transportation law but offer a wide range of services to our clients. We would like the design to be modern, simple, and professional. Our colors are black and gold, however, we've incorporated dark gray and white on other marketing products such as our website.

```html
<!DOCTYPE html>
<html lang="en">
<head>
<meta charset="utf-8">
<title>PDN Law Group Stationery</title>
<link href="https://fonts.googleapis.com/css2?family=Cinzel:wght@500&family=Roboto:wght@400;700&family=Open+Sans:wght@400&display=swap" rel="stylesheet">
<style>
:root{
  --gold:#a8895a;
  --black:#0c0c0c;
  --ink:#2a2a2a;
  --paper:#ffffff;
  --scene-a:#ebe9e7;
  --scene-b:#e7e7e7;
  --scene-c:#f0f0f0;
  --faint:#f1f1f1;
}
*{margin:0;padding:0;box-sizing:border-box}
html,body{width:1200px;height:2555px;overflow:hidden}
body{position:relative;font-family:'Roboto',sans-serif;color:var(--ink);background:var(--scene-b)}
.band{position:absolute;left:0;width:1200px}
.band-cards{top:0;height:965px;background:var(--scene-a)}
.band-letter{top:965px;height:800px;background:var(--scene-b)}
.band-envelopes{top:1765px;height:790px;background:var(--scene-c)}
.sheet{position:absolute;background:var(--paper);box-shadow:0 2px 10px rgba(0,0,0,.12);overflow:hidden}
.wordmark{font-family:'Cinzel',serif;font-weight:500;letter-spacing:2px;line-height:1.05;white-space:nowrap;text-align:center}
.wordmark .wordmark-sub{display:block;font-size:.5em;letter-spacing:.32em;margin-top:.25em}
.stripe{position:absolute;left:0;right:0;bottom:0;height:8px;display:flex}
.stripe .gold{background:var(--gold);flex:0 0 64%}
.stripe .black{background:var(--black);flex:1}
.contact{list-style:none;font-size:15px;line-height:1.35;color:var(--ink)}
.contact li{display:flex;align-items:center;gap:6px;white-space:nowrap}
.contact svg{width:12px;height:12px;fill:var(--ink);flex:none}

/* business cards */
.card-back{left:60px;top:140px;width:520px;height:290px;background:var(--black);display:flex;align-items:center;justify-content:center}
.card-back .wordmark{color:var(--paper);font-size:48px}
.card-front{left:620px;top:450px;width:520px;height:290px}
.card-front .wordmark{position:absolute;left:40px;top:100px;width:200px;color:var(--black);font-size:40px}
.card-front .divider{position:absolute;left:262px;top:70px;width:1px;height:130px;background:var(--ink)}
.card-front .person{position:absolute;left:282px;top:66px}
.person-name{font-weight:700;color:var(--gold);font-size:17px;letter-spacing:1px;text-transform:uppercase}
.person-role{font-weight:700;font-size:15px;margin-bottom:8px}

/* letterhead */
.letterhead{left:90px;top:1005px;width:540px;height:720px}
.letterhead .wordmark{position:absolute;left:44px;top:36px;color:var(--black);font-size:24px}
.letterhead .contact{position:absolute;left:380px;top:110px;font-size:8.5px;line-height:1.35;padding-left:8px;border-left:1px solid var(--ink)}
.letterhead .contact svg{width:7px;height:7px}
.letter-body{position:absolute;left:44px;top:196px;width:450px;font-family:'Open Sans',sans-serif;font-size:9px;line-height:1.5;color:#444}
.letter-body p{margin-bottom:9px}
.signature{width:70px;height:30px;background:linear-gradient(90deg,#e4e4e4,#f6f6f6);margin:8px 0 4px}

/* envelope flaps */
.flap{position:absolute;left:0;top:0;right:0;background:var(--black);border-bottom-right-radius:30px;display:flex;align-items:center;justify-content:center}
.envelope-back-small{left:670px;top:1265px;width:470px;height:220px}
.envelope-back-small .flap{height:72px}
.envelope-back-small .wordmark{color:var(--paper);font-size:18px}
.envelope-back-large{left:150px;top:1800px;width:830px;height:360px}
.envelope-back-large .flap{height:110px;border-bottom-right-radius:44px}
.envelope-back-large .wordmark{color:var(--paper);font-size:26px}

/* envelope front */
.envelope-front{left:110px;top:2200px;width:900px;height:330px}
.envelope-front .wordmark{position:absolute;left:130px;top:55px;color:var(--black);font-size:30px}
.envelope-front .contact{position:absolute;left:85px;top:200px;font-size:11px;line-height:1.35}
.envelope-front .contact svg{width:9px;height:9px}
.ghost-name{position:absolute;right:60px;top:120px;font-family:'Cinzel',serif;font-weight:500;font-size:150px;line-height:1;letter-spacing:6px;color:var(--faint);white-space:nowrap}
.envelope-front .stripe{height:10px}
</style>
</head>
<body>

<section class="band band-cards">
  <div class="sheet card-back">
    <div class="wordmark">PDN<span class="wordmark-sub">LAW GROUP</span></div>
  </div>
  <div class="sheet card-front">
    <div class="wordmark">PDN<span class="wordmark-sub">LAW GROUP</span></div>
    <div class="divider"></div>
    <div class="person">
      <div class="person-name">Daniel Porter</div>
      <div class="person-role">Director</div>
      <ul class="contact">
        <li>1820 Harbor Crest Avenue,</li>
        <li>Suite 210 Bayview.</li>
        <li><svg viewBox="0 0 12 12"><path d="M2 1h3l1 3-2 1a7 7 0 0 0 3 3l1-2 3 1v3a1 1 0 0 1-1 1A10 10 0 0 1 1 2a1 1 0 0 1 1-1z"/></svg>555.210.4400</li>
        <li><svg viewBox="0 0 12 12"><path d="M1 3h10v6H1z"/></svg>info@yourmail.com</li>
        <li><svg viewBox="0 0 12 12"><circle cx="6" cy="6" r="5"/></svg>www.yourwebsite.com</li>
      </ul>
    </div>
    <div class="stripe"><span class="gold"></span><span class="black"></span></div>
  </div>
</section>

<section class="band band-letter"></section>
<article class="sheet letterhead">
  <div class="wordmark">PDN<span class="wordmark-sub">LAW GROUP</span></div>
  <ul class="contact">
    <li>1820 Harbor Crest Avenue,</li>
    <li>Suite 210 Bayview.</li>
    <li><svg viewBox="0 0 12 12"><path d="M2 1h3l1 3-2 1a7 7 0 0 0 3 3l1-2 3 1v3a1 1 0 0 1-1 1A10 10 0 0 1 1 2a1 1 0 0 1 1-1z"/></svg>555.210.4400</li>
    <li><svg viewBox="0 0 12 12"><path d="M2 1h3l1 3-2 1a7 7 0 0 0 3 3l1-2 3 1v3a1 1 0 0 1-1 1A10 10 0 0 1 1 2a1 1 0 0 1 1-1z"/></svg>555.210.4411</li>
    <li><svg viewBox="0 0 12 12"><path d="M1 3h10v6H1z"/></svg>info@yourmail.com</li>
    <li><svg viewBox="0 0 12 12"><circle cx="6" cy="6" r="5"/></svg>www.yourwebsite.com</li>
  </ul>
  <div class="letter-body">
    <p>Dear customer,</p>
    <p>Lorem ipsum dolor sit amet, consectetur adipisicing elit, sed do eiusmod tempor incididunt ut labore et dolore magna aliqua. Ut enim ad minim veniam, quis nostrud exercitation ullamco laboris nisi ut aliquip ex ea commodo consequat. Duis aute irure dolor in reprehenderit in voluptate velit esse cillum dolore eu fugiat nulla pariatur. Excepteur sint occaecat cupidatat non proident, sunt in culpa qui officia deserunt mollit anim id est laborum.</p>
    <p>Lorem ipsum dolor sit amet, consectetur adipisicing elit, sed do eiusmod tempor incididunt ut labore et dolore magna aliqua. Ut enim ad minim veniam, quis nostrud exercitation ullamco laboris nisi ut aliquip ex ea commodo consequat. Duis aute irure dolor in reprehenderit in voluptate velit esse cillum dolore eu fugiat nulla pariatur. Excepteur sint occaecat cupidatat non proident, sunt in culpa qui officia deserunt mollit anim id est laborum.</p>
    <p>Lorem ipsum dolor sit amet, consectetur adipisicing elit, sed do eiusmod tempor incididunt ut labore et dolore magna aliqua. Ut enim ad minim veniam, quis nostrud exercitation ullamco laboris nisi ut aliquip ex ea commodo consequat. Duis aute irure dolor in reprehenderit in voluptate velit esse cillum dolore eu fugiat nulla pariatur. Excepteur sint occaecat cupidatat non proident, sunt in culpa qui officia deserunt mollit anim id est laborum.</p>
    <p>Lorem ipsum dolor sit amet, consectetur adipisicing elit, sed do eiusmod tempor incididunt ut labore et dolore magna aliqua. Ut enim ad minim veniam, quis nostrud exercitation ullamco laboris nisi ut aliquip ex ea commodo consequat. Duis aute irure dolor in reprehenderit.</p>
    <p>Yours Sincerely,</p>
    <div class="signature" role="img" aria-label="Handwritten signature"></div>
  </div>
  <div class="stripe"><span class="gold"></span><span class="black"></span></div>
</article>
<div class="sheet envelope-back-small">
  <div class="flap"><div class="wordmark">PDN</div></div>
</div>

<section class="band band-envelopes"></section>
<div class="sheet envelope-back-large">
  <div class="flap"><div class="wordmark">PDN</div></div>
</div>
<div class="sheet envelope-front">
  <div class="ghost-name" aria-hidden="true">PDN</div>
  <div class="wordmark">PDN<span class="wordmark-sub">LAW GROUP</span></div>
  <ul class="contact">
    <li>1820 Harbor Crest Avenue,</li>
    <li>Suite 210 Bayview.</li>
    <li><svg viewBox="0 0 12 12"><path d="M2 1h3l1 3-2 1a7 7 0 0 0 3 3l1-2 3 1v3a1 1 0 0 1-1 1A10 10 0 0 1 1 2a1 1 0 0 1 1-1z"/></svg>555.210.4400</li>
    <li><svg viewBox="0 0 12 12"><path d="M2 1h3l1 3-2 1a7 7 0 0 0 3 3l1-2 3 1v3a1 1 0 0 1-1 1A10 10 0 0 1 1 2a1 1 0 0 1 1-1z"/></svg>555.210.4411</li>
    <li><svg viewBox="0 0 12 12"><path d="M1 3h10v6H1z"/></svg>info@yourmail.com</li>
    <li><svg viewBox="0 0 12 12"><circle cx="6" cy="6" r="5"/></svg>www.yourwebsite.com</li>
  </ul>
  <div class="stripe"><span class="gold"></span><span class="black"></span></div>
</div>

</body>
</html>
```